Podcast cover design for a new podcast called 'Island Bright Voices'

I would like a clean, professional and impactful design for a new podcast I am launching called 'Island Bright Voices'. 'Island Bright Voices,' is a podcast featuring conversations with the island's groundbreaking entrepreneurs, technologists, artists, and scientists. Each episode uncovers the stories and insights of visionaries who are shaping Taiwan's future through cutting-edge startups, technological breakthroughs, artistic innovation, and scientific discovery. The podcast cover needs to look professional and be impactful. Ideally, I would also like the podcast cover to feature an photo or image of myself. Please see uploaded two recent photos of myself which you can crop etc for the podcast cover.

```html
<!DOCTYPE html>
<html lang="en">
<head>
<meta charset="utf-8">
<title>Island Bright Voices – Podcast Cover</title>
<link rel="stylesheet" href="https://fonts.googleapis.com/css2?family=Bebas+Neue&family=Signika:wght@600;700&display=swap">
<style>
  :root {
    --navy: #001040;
    --deep-blue: #03206a;
    --mid-blue: #0a3a9a;
    --glow-blue: #1d6fd6;
    --band-blue: #0b2c7c;
    --red: #ed1c24;
    --white: #ffffff;
  }
  * { margin: 0; padding: 0; box-sizing: border-box; }
  html, body { width: 1200px; height: 1200px; overflow: hidden; background: var(--navy); }
  .cover {
    position: relative;
    width: 1200px;
    height: 1200px;
    overflow: hidden;
  }
  .backdrop {
    position: absolute;
    inset: 0;
    background:
      radial-gradient(circle at 18% 30%, rgba(29,111,214,0.55), transparent 45%),
      radial-gradient(circle at 85% 20%, rgba(29,111,214,0.35), transparent 40%),
      radial-gradient(circle at 70% 60%, rgba(10,58,154,0.5), transparent 50%),
      linear-gradient(160deg, var(--mid-blue) 0%, var(--deep-blue) 55%, var(--navy) 100%);
  }
  .title-block {
    position: absolute;
    display: flex;
    align-items: center;
    justify-content: center;
    font-family: "Bebas Neue", "Arial Narrow", sans-serif;
    color: var(--white);
    font-size: 228px;
    line-height: 1;
    letter-spacing: 4px;
    padding-top: 18px;
  }
  .title-top { left: 130px; top: 62px; width: 895px; height: 237px; background: var(--navy); }
  .title-mid { left: 252px; top: 299px; width: 664px; height: 226px; background: var(--red); }
  .title-bottom { left: 184px; top: 527px; width: 794px; height: 236px; background: var(--navy); }
  .tagline {
    position: absolute;
    left: 0;
    top: 818px;
    width: 890px;
    text-align: center;
    font-family: "Signika", "Trebuchet MS", sans-serif;
    font-weight: 600;
    font-size: 58px;
    line-height: 70px;
    color: var(--white);
  }
  .host-band {
    position: absolute;
    left: 0;
    top: 1028px;
    width: 1200px;
    height: 172px;
    background: var(--band-blue);
  }
  .host-name {
    position: absolute;
    left: 0;
    top: 1066px;
    width: 900px;
    text-align: center;
    font-family: "Signika", "Trebuchet MS", sans-serif;
    font-weight: 700;
    font-size: 74px;
    line-height: 1;
    color: var(--white);
  }
  .host-portrait {
    position: absolute;
    left: 845px;
    top: 823px;
    width: 328px;
    height: 328px;
    border-radius: 50%;
    border: 8px solid var(--white);
    background: radial-gradient(circle at 50% 40%, #c89a84 0%, #8a6a55 28%, #2f5a2a 55%, #1a2a1a 100%);
  }
</style>
</head>
<body>
  <main class="cover">
    <div class="backdrop" role="img" aria-label="Abstract blue technology background with glowing circuit and lens shapes"></div>

    <h1>
      <span class="title-block title-top">ISLAND</span>
      <span class="title-block title-mid">BRIGHT</span>
      <span class="title-block title-bottom">VOICES</span>
    </h1>

    <p class="tagline">Inspiring Stories from Taiwan's<br>Leading Innovators</p>

    <div class="host-band"></div>
    <p class="host-name">with Julian Ashcombe</p>

    <div class="host-portrait" role="img" aria-label="Portrait photo of the host in a dark blazer against green foliage"></div>
  </main>
</body>
</html>
```